KORBALT

The business want a professional looking business card. We have a scetch we will add but want the extra upgrade, and would like more suggestions for variations of our business cards.

```html
<!DOCTYPE html>
<html lang="en">
<head>
<meta charset="utf-8">
<title>KORBALT – Business Card</title>
<link href="https://fonts.googleapis.com/css2?family=Cinzel:wght@400;600&family=Montserrat:wght@400;500&display=swap" rel="stylesheet">
<style>
  :root {
    --page-bg: #efeeeb;
    --card-bg: #ffffff;
    --gold: #a8782f;
    --brown: #4a3520;
    --ink: #2e2a26;
  }
  * { margin: 0; padding: 0; box-sizing: border-box; }
  html, body { width: 1200px; height: 1200px; overflow: hidden; }
  body { background: var(--page-bg); position: relative; font-family: "Montserrat", sans-serif; }

  .card { position: absolute; left: 108px; width: 978px; background: var(--card-bg); }
  .card--front { top: 100px; height: 500px; }
  .card--back { top: 658px; height: 445px; }

  /* Front */
  .brand-dot {
    position: absolute; top: 140px; left: 465px; width: 48px; height: 48px;
    border-radius: 50%; background: var(--gold);
  }
  .brand-name {
    position: absolute; top: 284px; left: 0; width: 100%; text-align: center;
    font-family: "Cinzel", serif; font-weight: 400; font-size: 100px; line-height: 1;
    letter-spacing: 0.02em; color: var(--gold);
  }
  .since {
    position: absolute; top: 391px; left: 0; width: 100%;
    display: flex; justify-content: center; align-items: center; gap: 26px;
    font-family: "Montserrat", sans-serif; font-size: 22px; font-weight: 500;
    letter-spacing: 0.42em; color: var(--gold);
  }
  .since__rule { width: 58px; height: 2px; background: var(--gold); }
  .since__text { margin-right: -0.42em; }

  /* Back */
  .person-name {
    position: absolute; left: 98px; top: 76px;
    font-family: "Cinzel", serif; font-weight: 600; font-size: 36px;
    letter-spacing: 0.04em; color: var(--brown); line-height: 1;
  }
  .person-title {
    position: absolute; left: 99px; top: 138px;
    font-size: 20px; letter-spacing: 0.3em; color: var(--brown); line-height: 1;
  }
  .title-rule { position: absolute; left: 99px; top: 191px; width: 82px; height: 2px; background: var(--gold); }

  .contact-list { position: absolute; left: 98px; top: 228px; list-style: none; }
  .contact-item { display: flex; align-items: center; height: 55px; font-size: 23px; color: var(--ink); }
  .contact-icon { width: 34px; height: 34px; margin-right: 30px; flex: none; }
  .contact-icon * { fill: none; stroke: var(--gold); stroke-width: 2.2; stroke-linecap: round; stroke-linejoin: round; }

  .divider { position: absolute; left: 697px; top: 63px; width: 2px; height: 317px; background: var(--gold); }
  .side-brand {
    position: absolute; left: 733px; top: 204px; width: 200px; text-align: center;
    font-family: "Cinzel", serif; font-weight: 400; font-size: 32px; line-height: 1;
    color: var(--gold);
  }
</style>
</head>
<body>
  <section class="card card--front">
    <div class="brand-dot"></div>
    <h1 class="brand-name">KORBALT</h1>
    <div class="since">
      <span class="since__rule"></span>
      <span class="since__text">SINCE 2026</span>
      <span class="since__rule"></span>
    </div>
  </section>

  <section class="card card--back">
    <h2 class="person-name">MATS OLAV BRENHEIM</h2>
    <p class="person-title">CEO &amp; FOUNDER</p>
    <div class="title-rule"></div>

    <ul class="contact-list">
      <li class="contact-item">
        <svg class="contact-icon" viewBox="0 0 34 34" aria-hidden="true">
          <path d="M8 5 L13 5 L15 12 L11.5 14.5 C13.5 19 15.5 21 20 23 L22.5 19.5 L29 21.5 L29 26.5 C29 28 27.5 29 26 29 C15 28 6 19 5 8 C5 6.5 6.5 5 8 5 Z"/>
        </svg>
        <span>004795550142</span>
      </li>
      <li class="contact-item">
        <svg class="contact-icon" viewBox="0 0 34 34" aria-hidden="true">
          <rect x="3" y="8" width="28" height="19"/>
          <path d="M3 8 L17 19 L31 8"/>
        </svg>
        <span>korbalt.studio@mailbox.no</span>
      </li>
      <li class="contact-item">
        <svg class="contact-icon" viewBox="0 0 34 34" aria-hidden="true">
          <circle cx="17" cy="17" r="14"/>
          <ellipse cx="17" cy="17" rx="6" ry="14"/>
          <path d="M3 17 H31 M5.5 10 H28.5 M5.5 24 H28.5 M17 3 V31"/>
        </svg>
        <span>www.korbalt.llc</span>
      </li>
    </ul>

    <div class="divider"></div>
    <p class="side-brand">KORBALT</p>
  </section>
</body>
</html>
```